Live a healthy life. Kvel

Advertising campaign for reversing type 2 diabetes and insulin resistance. The best way to reverse type 2 diabetes or put it in remission is to prevent it from triggering. We do this by healthy food choices, no overeating and exercise. The final design should promote the aforementioned and should be able to be implemented in society, schools, churches etc. Kvel is the creator of the campaign. Youtube channel "straight from the desk of Kvel"

```html
<!DOCTYPE html>
<html lang="en">
<head>
<meta charset="utf-8">
<title>Live a healthy life – Kvel</title>
<link href="https://fonts.googleapis.com/css2?family=Montserrat:ital,wght@0,300;0,700;0,800;0,900;1,900&family=Roboto+Condensed:wght@700;800&display=swap" rel="stylesheet">
<style>
  :root {
    --navy-1: #3d3383;
    --navy-2: #231862;
    --lilac-head: #c3bdfb;
    --ice-head: #dde6fb;
    --white: #ffffff;
    --alert-red: #f40000;
    --ribbon-dark: #b00000;
    --ring-1: #d9d6fa;
    --ring-2: #e3e1fb;
    --ring-3: #eceafc;
    --ring-4: #f4f3fd;
    --ink-violet: #4b4fae;
    --ink-blue: #2f73cc;
    --art-violet: #6a5fd0;
    --art-red: #e8505a;
  }
  * { margin: 0; padding: 0; box-sizing: border-box; }
  html, body { width: 848px; height: 1200px; overflow: hidden; background: var(--ring-1); }
  .poster {
    position: relative; width: 848px; height: 1200px; overflow: hidden;
    font-family: "Montserrat", sans-serif;
    background:
      radial-gradient(circle at 50% 640px,
        var(--ring-4) 0 230px, var(--ring-3) 230px 330px,
        var(--ring-2) 330px 420px, var(--ring-1) 420px);
  }
  .header-band { position: absolute; left: 0; top: 0; width: 848px; height: 430px; }
  .headline {
    position: absolute; left: 0; top: 36px; width: 848px;
    text-align: center; color: var(--white); line-height: 1;
  }
  .headline .line { display: block; white-space: nowrap; }
  .headline .light { font-weight: 300; }
  .headline .strong { font-weight: 900; letter-spacing: -1px; }
  .line-1 { font-size: 76px; }
  .line-1 .strong { color: var(--lilac-head); margin: 0 14px; }
  .line-2 { font-size: 76px; margin-top: -2px; }
  .line-2 .reverse { color: var(--lilac-head); }
  .line-2 .type { color: var(--ice-head); }
  .line-3 { font-size: 74px; margin-top: 2px; }
  .line-3 .strong { color: var(--ice-head); }
  .line-3 .light { color: var(--ice-head); }
  .line-4 { font-size: 76px; margin-top: 4px; position: relative; left: -4px; }
  .trigger-tag {
    display: inline-block; background: var(--alert-red);
    font-weight: 900; font-style: italic; color: var(--white);
    padding: 6px 26px 10px 18px; margin-left: 8px; letter-spacing: -1px;
  }
  .method {
    position: absolute; left: 0; top: 478px; width: 848px; text-align: center;
    line-height: 1.08; white-space: nowrap;
  }
  .method span {
    background: linear-gradient(90deg, var(--ink-violet) 30%, var(--ink-blue));
    -webkit-background-clip: text; background-clip: text; color: transparent;
  }
  .method .intro { display: block; font-size: 58px; font-weight: 300; }
  .method .key { display: block; font-size: 63px; font-weight: 800; letter-spacing: -1px; }
  .method .key .thin { font-weight: 300; letter-spacing: 0; }
  .care-kit {
    position: absolute; left: 70px; top: 780px; width: 730px; height: 300px;
    border-radius: 40px 40px 0 0;
    background: linear-gradient(100deg, var(--art-violet) 0%, #8f86e6 35%, var(--art-red) 60%, #9d93ea 100%);
    opacity: 0.85;
  }
  .signature-name {
    position: absolute; left: 330px; top: 880px; width: 240px;
    text-align: center; font-weight: 800; font-size: 30px; line-height: 1.1;
    color: var(--white);
  }
  .ribbon { position: absolute; left: 0; top: 1050px; width: 848px; height: 150px; }
  .ribbon-label {
    position: absolute; left: 97px; top: 1104px; width: 653px; text-align: center;
    font-family: "Roboto Condensed", sans-serif; font-weight: 800;
    font-size: 49px; color: var(--white); letter-spacing: -1px; white-space: nowrap;
  }
</style>
</head>
<body>
<main class="poster">
  <svg class="header-band" viewBox="0 0 848 430" aria-hidden="true">
    <defs>
      <linearGradient id="bandFill" x1="0" y1="0" x2="1" y2="1">
        <stop offset="0" stop-color="#3d3383"/>
        <stop offset="1" stop-color="#231862"/>
      </linearGradient>
    </defs>
    <path d="M0 0 H848 V373 Q424 470 0 380 Z" fill="url(#bandFill)"/>
  </svg>

  <h1 class="headline">
    <span class="line line-1"><span class="light">The</span><span class="strong">Best Way</span><span class="light">to</span></span>
    <span class="line line-2"><span class="strong reverse">Reverse</span> <span class="strong type">Type 2</span></span>
    <span class="line line-3"><span class="strong">Diabetes</span> <span class="light">is to prevent</span></span>
    <span class="line line-4"><span class="light">it from</span><span class="trigger-tag">triggering</span></span>
  </h1>

  <p class="method">
    <span class="intro">We do this by</span>
    <span class="key">healthy food choices,</span>
    <span class="key">no overeating</span>
    <span class="key"><span class="thin">and</span> exercise</span>
  </p>

  <div class="care-kit" role="img" aria-label="Illustration of a glucose meter, test tube, clipboard, medicine bottle, capsules and leaves"></div>
  <p class="signature-name">straight from the desk of Kvel</p>

  <svg class="ribbon" viewBox="0 1050 848 150" aria-hidden="true">
    <polygon points="20,1053 182,1053 182,1147 20,1147 48,1100" fill="#f40000"/>
    <polygon points="828,1053 666,1053 666,1147 828,1147 800,1100" fill="#f40000"/>
    <polygon points="97,1097 182,1097 182,1147 97,1147" fill="#b00000"/>
    <polygon points="666,1097 750,1097 750,1147 666,1147" fill="#b00000"/>
    <rect x="97" y="1097" width="653" height="96" fill="#f40000"/>
  </svg>
  <p class="ribbon-label">Creator of the campaign Kvel</p>
</main>
</body>
</html>
```